" Somos um eccomerce de iluminação led. temos um portfólio muito vasto de produtos para atender diversas demandas: consumidor final, revenda, condomínios e empresas no modo geral. "

```html
<!DOCTYPE html>
<html lang="pt-BR">
<head>
<meta charset="utf-8">
<title>Catálogo 2018 – Iluminação LED</title>
<link rel="stylesheet" href="https://fonts.googleapis.com/css2?family=Open+Sans:ital,wght@0,400;0,600;0,700;1,700;1,800&display=swap">
<style>
  :root {
    --bg: #2b2b2b;
    --paper: #f5f5f5;
    --paper-shade: #e9e9e9;
    --ink: #2d2d2d;
    --muted: #6f6f6f;
    --row: #e4e4e4;
    --row-alt: #efefef;
    --red: #a8262b;
    --teal: #5aa3ab;
    --icon: #3a3a3a;
  }
  * { box-sizing: border-box; margin: 0; padding: 0; }
  html, body { width: 1200px; height: 1200px; overflow: hidden; }
  body { background: var(--bg); font-family: "Open Sans", Arial, sans-serif; color: var(--ink); position: relative; }

  .spread { position: absolute; left: 50px; top: 212px; width: 1100px; height: 776px; display: flex; box-shadow: 0 10px 30px rgba(0,0,0,.5); }
  .page { position: relative; width: 550px; height: 776px; background: var(--paper); overflow: hidden; }
  .page--left { background: linear-gradient(to right, var(--paper) 90%, var(--paper-shade)); }
  .page--right { background: linear-gradient(to left, var(--paper) 90%, var(--paper-shade)); }

  .hero { position: absolute; left: 0; top: 0; width: 100%; height: 150px; }
  .hero--ceiling { background: linear-gradient(180deg, #cfc4b6 0%, #e6ddd2 55%, #f5f5f5 100%); }
  .hero--facade { background: linear-gradient(180deg, #a88d6c 0%, #d8c6ad 55%, #f5f5f5 100%); }

  .spine { position: absolute; top: 0; bottom: 0; width: 26px; display: flex; align-items: center; justify-content: center; }
  .page--left .spine { right: 0; background: var(--red); }
  .page--right .spine { right: 0; background: var(--teal); }
  .spine span { writing-mode: vertical-rl; transform: rotate(180deg); color: #fff; font-size: 9px; letter-spacing: .5px; white-space: nowrap; }
  .spine b { font-weight: 700; }

  .section { position: absolute; left: 42px; width: 450px; }
  .section-head { display: flex; align-items: center; gap: 10px; border-bottom: 1px solid #bdbdbd; padding-bottom: 6px; }
  .section-head::before { content: ""; width: 28px; height: 1px; background: #bdbdbd; align-self: center; }
  .section-title { font-style: italic; font-weight: 800; font-size: 21px; color: var(--ink); }
  .tag { color: #fff; font-size: 12px; padding: 3px 9px; }
  .tag--red { background: var(--red); }
  .tag--teal { background: var(--teal); }

  .features { display: flex; gap: 22px; margin-top: 12px; font-size: 8.5px; font-weight: 700; }
  .feature { display: flex; align-items: center; gap: 5px; }
  .feature svg { width: 12px; height: 12px; }

  .product { display: flex; gap: 22px; margin-top: 12px; }
  .product-visual { width: 120px; }
  .ref { font-size: 8px; color: var(--muted); margin-bottom: 6px; }
  .product-shot { width: 110px; height: 110px; }

  .specs { border-collapse: collapse; font-size: 8.5px; width: 300px; margin-top: 6px; }
  .specs td { height: 20px; padding: 0 8px; }
  .specs tr:nth-child(odd) td { background: var(--row); }
  .specs tr:nth-child(even) td { background: var(--row-alt); }
  .specs td:first-child { width: 92px; color: var(--muted); }

  .folio { position: absolute; bottom: 16px; font-size: 10px; color: var(--muted); }
  .page--left .folio { left: 22px; }
  .page--right .folio { left: 22px; }
</style>
</head>
<body>
<div class="spread">

  <section class="page page--left">
    <div class="hero hero--ceiling" role="img" aria-label="Foto de teto de ambiente interno iluminado por luminárias embutidas"></div>
    <div class="spine"><span><b>Luminárias LED</b> | Catálogo 2018</span></div>

    <article class="section" style="top:170px">
      <header class="section-head"><h2 class="section-title">Luminárias Plafon</h2><span class="tag tag--red">Sobrepor</span></header>
      <ul class="features">
        <li class="feature"><svg viewBox="0 0 12 12"><rect width="12" height="12" rx="2" fill="var(--icon)"/><path d="M3 6l2 2 4-4" stroke="#fff" stroke-width="1.4" fill="none"/></svg>Garantia de 1 ano</li>
        <li class="feature"><svg viewBox="0 0 12 12"><rect width="12" height="12" rx="2" fill="var(--icon)"/><path d="M6 2.5l3 1.2v2.5c0 1.8-1.4 3-3 3.5-1.6-.5-3-1.7-3-3.5V3.7z" fill="#fff"/></svg>Índice de Proteção IP 65</li>
        <li class="feature"><svg viewBox="0 0 12 12"><rect width="12" height="12" rx="2" fill="var(--icon)"/><circle cx="6" cy="6" r="3.3" stroke="#fff" fill="none"/><path d="M6 4v2.2h1.6" stroke="#fff" fill="none"/></svg>Vida Útil de 25.000 horas</li>
      </ul>
      <div class="product">
        <div class="product-visual"><p class="ref">Ref. 123456</p><div class="product-shot" role="img" aria-label="Foto da luminária plafon de sobrepor quadrada e redonda" style="background:radial-gradient(circle,#ffffff 45%,#dcdcdc 100%)"></div></div>
        <table class="specs">
          <tr><td>Potência</td><td>6w, 12w, 18w, 25w, 30w, 42w, 48w</td></tr>
          <tr><td>Cor da Luz</td><td>Branco Frio, Branco Quente</td></tr>
          <tr><td>Formato</td><td>Quadrado, Redondo</td></tr>
          <tr><td>Material</td><td>Acrílico e Alumínio</td></tr>
          <tr><td>Voltagem</td><td>Bivolt Automático (110v - 220v)</td></tr>
          <tr><td>Tamanho</td><td>17cm, 22cm, 30cm, 40cm</td></tr>
        </table>
      </div>
    </article>

    <article class="section" style="top:470px">
      <header class="section-head"><h2 class="section-title">Luminárias Plafon</h2><span class="tag tag--red">Embutir</span></header>
      <ul class="features">
        <li class="feature"><svg viewBox="0 0 12 12"><rect width="12" height="12" rx="2" fill="var(--icon)"/><path d="M3 6l2 2 4-4" stroke="#fff" stroke-width="1.4" fill="none"/></svg>Garantia de 1 ano</li>
        <li class="feature"><svg viewBox="0 0 12 12"><rect width="12" height="12" rx="2" fill="var(--icon)"/><path d="M6 2.5l3 1.2v2.5c0 1.8-1.4 3-3 3.5-1.6-.5-3-1.7-3-3.5V3.7z" fill="#fff"/></svg>Índice de Proteção IP 65</li>
        <li class="feature"><svg viewBox="0 0 12 12"><rect width="12" height="12" rx="2" fill="var(--icon)"/><circle cx="6" cy="6" r="3.3" stroke="#fff" fill="none"/><path d="M6 4v2.2h1.6" stroke="#fff" fill="none"/></svg>Vida Útil de 25.000 horas</li>
      </ul>
      <div class="product">
        <div class="product-visual"><p class="ref">Ref. 123456</p><div class="product-shot" role="img" aria-label="Foto da luminária plafon de embutir quadrada e redonda" style="background:radial-gradient(circle,#ffffff 45%,#dcdcdc 100%)"></div></div>
        <table class="specs">
          <tr><td>Potência</td><td>6w, 12w, 18w, 25w, 30w, 42w, 48w</td></tr>
          <tr><td>Cor da Luz</td><td>Branco Frio, Branco Quente</td></tr>
          <tr><td>Formato</td><td>Quadrado, Redondo</td></tr>
          <tr><td>Material</td><td>Acrílico e Alumínio</td></tr>
          <tr><td>Voltagem</td><td>Bivolt Automático (110v - 220v)</td></tr>
          <tr><td>Tamanho</td><td>17cm, 22cm, 30cm, 40cm</td></tr>
        </table>
      </div>
    </article>

    <span class="folio">03</span>
  </section>

  <section class="page page--right">
    <div class="hero hero--facade" role="img" aria-label="Foto de fachada iluminada por refletores LED"></div>
    <div class="spine"><span><b>Refletores LED</b> | Catálogo 2018</span></div>

    <article class="section" style="top:170px">
      <header class="section-head"><h2 class="section-title">Refletores LED</h2><span class="tag tag--teal">Super LED</span></header>
      <ul class="features">
        <li class="feature"><svg viewBox="0 0 12 12"><rect width="12" height="12" rx="2" fill="var(--icon)"/><path d="M3 6l2 2 4-4" stroke="#fff" stroke-width="1.4" fill="none"/></svg>Garantia de 1 ano</li>
        <li class="feature"><svg viewBox="0 0 12 12"><rect width="12" height="12" rx="2" fill="var(--icon)"/><path d="M6 2.5l3 1.2v2.5c0 1.8-1.4 3-3 3.5-1.6-.5-3-1.7-3-3.5V3.7z" fill="#fff"/></svg>Índice de Proteção IP 65</li>
        <li class="feature"><svg viewBox="0 0 12 12"><rect width="12" height="12" rx="2" fill="var(--icon)"/><circle cx="6" cy="6" r="3.3" stroke="#fff" fill="none"/><path d="M6 4v2.2h1.6" stroke="#fff" fill="none"/></svg>Vida Útil de 25.000 horas</li>
      </ul>
      <div class="product">
        <div class="product-visual"><p class="ref">Ref. 123456</p><div class="product-shot" role="img" aria-label="Foto do refletor Super LED" style="background:linear-gradient(160deg,#4a4a4a,#1e1e1e)"></div></div>
        <table class="specs">
          <tr><td>Potência</td><td>6w, 12w, 18w, 25w, 30w, 42w, 48w</td></tr>
          <tr><td>Cor da Luz</td><td>Branco Frio, Branco Quente</td></tr>
          <tr><td>Formato</td><td>Quadrado, Redondo</td></tr>
          <tr><td>Material</td><td>Acrílico e Alumínio</td></tr>
          <tr><td>Voltagem</td><td>Bivolt Automático (110v - 220v)</td></tr>
          <tr><td>Tamanho</td><td>17cm, 22cm, 30cm, 40cm</td></tr>
        </table>
      </div>
    </article>

    <article class="section" style="top:470px">
      <header class="section-head"><h2 class="section-title">Refletores LED</h2><span class="tag tag--teal">Micro LED Ultra</span></header>
      <ul class="features">
        <li class="feature"><svg viewBox="0 0 12 12"><rect width="12" height="12" rx="2" fill="var(--icon)"/><path d="M3 6l2 2 4-4" stroke="#fff" stroke-width="1.4" fill="none"/></svg>Garantia de 1 ano</li>
        <li class="feature"><svg viewBox="0 0 12 12"><rect width="12" height="12" rx="2" fill="var(--icon)"/><path d="M6 2.5l3 1.2v2.5c0 1.8-1.4 3-3 3.5-1.6-.5-3-1.7-3-3.5V3.7z" fill="#fff"/></svg>Índice de Proteção IP 65</li>
        <li class="feature"><svg viewBox="0 0 12 12"><rect width="12" height="12" rx="2" fill="var(--icon)"/><circle cx="6" cy="6" r="3.3" stroke="#fff" fill="none"/><path d="M6 4v2.2h1.6" stroke="#fff" fill="none"/></svg>Vida Útil de 25.000 horas</li>
      </ul>
      <div class="product">
        <div class="product-visual"><p class="ref">Ref. 123456</p><div class="product-shot" role="img" aria-label="Foto do refletor Micro LED Ultra" style="background:linear-gradient(160deg,#3a3a3a,#111)"></div></div>
        <table class="specs">
          <tr><td>Potência</td><td>6w, 12w, 18w, 25w, 30w, 42w, 48w</td></tr>
          <tr><td>Cor da Luz</td><td>Branco Frio, Branco Quente</td></tr>
          <tr><td>Formato</td><td>Quadrado, Redondo</td></tr>
          <tr><td>Material</td><td>Acrílico e Alumínio</td></tr>
          <tr><td>Voltagem</td><td>Bivolt Automático (110v - 220v)</td></tr>
          <tr><td>Tamanho</td><td>17cm, 22cm, 30cm, 40cm</td></tr>
        </table>
      </div>
    </article>

    <span class="folio">04</span>
  </section>

</div>
</body>
</html>
```